Website design for KORVEL – data platform for healthcare & social housing

We’re looking for a clean, modern multi-page website design for KORVEL — a data platform for healthcare and social housing.

📎 Please read the attached PDF for full structure, context, and design guidance.
The briefing is essential to understanding this project.

➡️ For the initial submission, only the homepage design (including header and footer) is required.

This will help us assess design direction and fit.

The full project includes four levels (homepage, general page, product overview, and product detail), which will be completed after selecting the final designer.

Industry/Entity Type

data platform for healthcare & social housing

Number of Pages Required

1 page

Font styles to use
Sans Serif

Requirements
Must have
• Please read the attached PDF
Nice to have
Should not have

```html
<!DOCTYPE html>
<html lang="en">
<head>
<meta charset="utf-8">
<title>KORVEL – Data platform for Healthcare and Social Housing</title>
<link href="https://fonts.googleapis.com/css2?family=Archivo:wght@500;600;700&family=Arimo:wght@400;700&display=swap" rel="stylesheet">
<style>
:root{
  --navy:#0c3b78;
  --navy-dark:#0a3169;
  --orange:#f47a1f;
  --cyan:#7dd9e9;
  --cyan-line:#9fd7ea;
  --teal:#2bb0c1;
  --ink:#1d2430;
  --muted:#4b5563;
  --pale:#eef8fc;
  --white:#ffffff;
}
*{box-sizing:border-box;margin:0;padding:0}
html,body{width:1200px;height:3752px;overflow:hidden}
body{font-family:"Arimo",Arial,sans-serif;color:var(--ink);background:var(--white);position:relative}
.abs{position:absolute}
.h2{font-family:"Archivo",Arial,sans-serif;font-weight:600;font-size:29px;letter-spacing:.5px;text-transform:uppercase;color:var(--ink);white-space:nowrap}
.title-line{display:flex;align-items:center;justify-content:center;gap:10px}
.title-line .rule{width:58px;height:2px;background:var(--orange);position:relative}
.title-line .rule::before{content:"";position:absolute;top:-2px;width:6px;height:6px;border-radius:50%;background:var(--orange)}
.title-line .rule.l::before{left:-3px}
.title-line .rule.r::before{right:-3px}
.btn{position:absolute;display:flex;align-items:center;justify-content:space-between;padding:0 14px;height:40px;font-family:"Archivo",Arial,sans-serif;font-weight:600;font-size:12px;letter-spacing:.4px;color:#fff;text-transform:uppercase;background:var(--orange);white-space:nowrap}
.btn::after{content:"";flex:none;width:5px;height:5px;border-radius:50%;background:currentColor;margin-left:10px}
.btn.navy{background:#174a94}
.btn.teal{background:var(--teal)}
.btn.white{background:#fff;color:var(--navy)}

/* header */
.site-header{position:absolute;top:0;left:0;width:1200px;height:56px;background:#fff;border-top:2px solid var(--orange)}
.brand{position:absolute;font-family:"Archivo",Arial,sans-serif;font-weight:700;letter-spacing:4px}
.site-header .brand{left:122px;top:12px;font-size:24px;color:var(--navy)}
.nav{position:absolute;left:314px;top:22px;display:flex;gap:16px;font-family:"Archivo",Arial,sans-serif;font-weight:600;font-size:11px;color:var(--navy);text-transform:uppercase;white-space:nowrap}
.site-header .btn{height:31px;top:13px;font-size:11px;padding:0 12px}

/* hero */
.hero{position:absolute;top:56px;left:0;width:1200px;height:585px;background:linear-gradient(90deg,#a9b8c6 0%,#dfe5ea 30%,#c9ced2 55%,#8c949c 80%,#b6b8b6 100%)}
.hero::after{content:"";position:absolute;inset:0;background:rgba(20,40,70,.25)}
.hero-copy{position:absolute;z-index:2;top:292px;width:1200px;text-align:center;color:#fff}
.hero-copy h1{font-family:"Archivo",Arial,sans-serif;font-weight:600;font-size:42px;line-height:52px;text-transform:uppercase;letter-spacing:.5px}
.hero-copy p{margin-top:10px;font-size:15px}
.hero .btn{z-index:2}

/* what is */
.what-media{position:absolute;left:122px;top:685px;width:460px;height:316px}
.what-copy{position:absolute;left:650px;top:688px;width:370px}
.what-copy p{font-size:11px;line-height:17px;color:var(--muted);margin-top:14px}
.sector{position:absolute;display:flex;align-items:center;gap:8px;font-family:"Archivo",Arial,sans-serif;font-weight:600;font-size:12.5px;color:var(--navy);white-space:nowrap}
.sector .ico{width:42px;height:42px;border-radius:50%;background:var(--teal);display:flex;align-items:center;justify-content:center}

/* how helps */
.how-band{position:absolute;left:0;top:1175px;width:1200px;height:125px;background:var(--cyan)}
.how-pill{position:absolute;left:200px;top:1088px;width:800px;height:294px;border-radius:147px;background:var(--cyan)}
.ring{position:absolute;width:206px;height:206px;border-radius:50%;background:#fff;border:3px solid #e9f7fb;display:flex;flex-direction:column;align-items:center;justify-content:center;text-align:center;font-family:"Archivo",Arial,sans-serif;font-weight:600;font-size:15px;color:var(--ink);text-transform:uppercase;line-height:18px}
.ring svg{margin-bottom:4px}
.ring .stem{width:2px;height:18px;background:var(--orange);position:relative;margin:2px 0 12px}
.ring .stem::after{content:"";position:absolute;left:-2px;bottom:-3px;width:6px;height:6px;border-radius:50%;background:var(--orange)}
.bump{position:absolute;left:482px;top:1368px;width:236px;height:60px;border-radius:30px 30px 0 0;background:#fff}

/* products */
.products{position:absolute;left:0;top:1485px;width:1200px;height:558px;background:var(--pale)}
.card{position:absolute;top:1663px;width:224px;height:258px;border-radius:4px;overflow:hidden}
.card span{position:absolute;bottom:20px;width:100%;text-align:center;color:#fff;font-family:"Archivo",Arial,sans-serif;font-weight:600;font-size:14.5px;letter-spacing:.4px}
.pin{position:absolute;top:1643px;width:40px;height:40px;border-radius:50%;background:var(--teal);border:3px solid #fff;display:flex;align-items:center;justify-content:center;z-index:2}

/* who for */
.who{position:absolute;width:200px;height:200px;border-radius:50%;background:#fff;border:1.5px solid #3f86c6;box-shadow:0 6px 0 -1px var(--cyan);display:flex;flex-direction:column;align-items:center;justify-content:center;text-align:center;font-family:"Archivo",Arial,sans-serif;font-weight:600;font-size:15px;line-height:18px;text-transform:uppercase}
.who .stem{width:2px;height:18px;background:var(--orange);position:relative;margin:4px 0 14px}
.who .stem::after{content:"";position:absolute;left:-2px;bottom:-3px;width:6px;height:6px;border-radius:50%;background:var(--orange)}

/* community */
.community{position:absolute;left:0;top:2425px;width:1200px;height:403px;background:linear-gradient(90deg,#b99683 0%,#e0c3ad 30%,#f5e6d8 55%,#fbeee3 80%,#fcd9b0 100%)}
.community-copy{position:absolute;left:687px;top:2545px;width:380px}
.community-copy .h2{font-size:28px}
.community-copy p{font-size:11px;line-height:17px;color:var(--muted);margin-top:14px}

/* clients */
.quote{position:absolute;top:2942px;width:406px;height:226px;background:#fff;border:1.5px solid #5b93cf;box-shadow:0 2px 6px rgba(0,0,0,.08);padding:34px 32px}
.quote .head{display:flex;align-items:center;gap:16px}
.avatar{width:52px;height:52px;border-radius:50%;border:3px solid #8fd4e3;background:linear-gradient(#e8c8b0,#b98f73)}
.quote .name{font-family:"Archivo",Arial,sans-serif;font-weight:600;font-size:12px}
.stars{color:#f6b415;font-size:17px;letter-spacing:1px}
.quote .qm{position:absolute;right:18px;top:18px;font-family:Georgia,serif;font-size:90px;line-height:70px;color:#e6e8ea}
.quote p{margin-top:24px;font-size:11px;line-height:17.5px;color:var(--muted)}
.arrow{position:absolute;width:24px;height:24px;border-radius:50%;border:1.5px solid var(--teal);display:flex;align-items:center;justify-content:center}

/* cta */
.cta{position:absolute;left:0;top:3230px;width:1200px;height:275px;background:var(--teal)}
.cta .h2{color:#fff}
.cta .rule,.cta .rule::before{background:#fff}

/* footer */
.footer{position:absolute;left:0;top:3505px;width:1200px;height:247px;background:var(--navy);color:#fff}
.footer h4{font-family:"Archivo",Arial,sans-serif;font-weight:600;font-size:14px;letter-spacing:.6px;text-transform:uppercase}
.footer .col{position:absolute;top:60px}
.footer small{font-size:8.5px;line-height:16px;display:block}
.footer .divider{position:absolute;top:40px;width:1px;height:180px;background:rgba(255,255,255,.35)}
.contact-row{display:flex;align-items:center;gap:12px;font-size:8.5px;margin-top:12px;white-space:nowrap}
.contact-row .ci{width:24px;height:24px;border-radius:50%;border:1.5px solid #fff;display:flex;align-items:center;justify-content:center}
</style>
</head>
<body>

<header class="site-header">
  <div class="brand">KORVEL</div>
  <nav class="nav"><span>What is KORVEL?</span><span>Products</span><span>Who it's for</span><span>Community</span><span>About us</span><span>Contact</span></nav>
  <a class="btn teal" style="left:840px;width:120px">Plan a demo</a>
  <a class="btn" style="left:968px;width:109px">Start KORVEL</a>
</header>

<section class="hero" role="img" aria-label="Photo of a smiling doctor with a clipboard on the left and a woman studying housing plans next to a small house model on the right">
  <div class="hero-copy">
    <h1>More impact with better<br>control over data</h1>
    <p>Data analytics for Healthcare and Social Housing</p>
  </div>
  <a class="btn" style="left:458px;top:444px;width:138px">Products</a>
  <a class="btn navy" style="left:605px;top:444px;width:138px">Plan a demo</a>
</section>

<div class="what-media">
  <div class="abs" role="img" aria-label="Photo of a healthcare worker at a desk" style="left:40px;top:10px;width:380px;height:290px;border-radius:24px;background:linear-gradient(135deg,#2b3440,#c9ccd0 50%,#3a4a60)"></div>
  <div class="abs" role="img" aria-label="Photo of hands working on a laptop showing charts" style="left:125px;top:95px;width:215px;height:215px;border-radius:50%;border:6px solid var(--cyan);background:radial-gradient(circle at 50% 40%,#eef1f4,#c8b8a6 70%,#a68f7a)"></div>
</div>
<div class="what-copy">
  <div class="title-line" style="justify-content:flex-start"><span class="h2">What is KORVEL?</span><span class="rule r"></span></div>
  <p>KORVEL is a Data analytics Platform for the Healthcare sector and social housing sector. We centralize, analyze, and visualize the data that matters — turning insight into action.</p>
  <p>Whether you're tackling homelessness, hospital discharge delays, or housing quality, KORVEL gives you the tools to understand the full picture and respond with confidence.</p>
</div>
<div class="sector" style="left:650px;top:868px"><span class="ico"><svg width="24" height="24" viewBox="0 0 24 24" fill="none" stroke="#fff" stroke-width="1.6"><path d="M12 20s-8-5-8-11a4 4 0 0 1 8-1 4 4 0 0 1 8 1c0 6-8 11-8 11z"/><path d="M5 11h4l1.5-3 2 6 1.5-3h5"/></svg></span>Healthcare Sector</div>
<div class="sector" style="left:829px;top:868px"><span class="ico"><svg width="24" height="24" viewBox="0 0 24 24" fill="none" stroke="#fff" stroke-width="1.6"><path d="M3 11l9-7 9 7"/><path d="M6 9v11h12V9"/><path d="M10 20v-5h4v5"/></svg></span>Social Housing Sector</div>
<a class="btn" style="left:650px;top:938px;width:172px">What is KORVEL?</a>

<div class="abs title-line" style="left:0;top:1050px;width:1200px"><span class="rule l"></span><span class="h2">How KORVEL helps</span><span class="rule r"></span></div>
<div class="how-band"></div>
<div class="how-pill"></div>
<div class="ring" style="left:231px;top:1130px">
  <svg width="64" height="64" viewBox="0 0 64 64" fill="none" stroke="var(--navy)" stroke-width="2.5"><path d="M32 6 58 20 32 34 6 20z"/><path d="M6 30l26 14 26-14"/><path d="M6 40l26 14 26-14"/><path d="M20 20l12-6 12 6-12 6z"/></svg>
  <span class="stem"></span>Platform and<br>products</div>
<div class="ring" style="left:494px;top:1130px">
  <svg width="64" height="64" viewBox="0 0 64 64" fill="none" stroke="var(--navy)" stroke-width="2.5"><path d="M32 56S6 40 6 22a13 13 0 0 1 26-3 13 13 0 0 1 26 3c0 18-26 34-26 34z"/><circle cx="24" cy="24" r="5"/><circle cx="40" cy="24" r="5"/><circle cx="32" cy="36" r="5"/></svg>
  <span class="stem"></span>Community</div>
<div class="ring" style="left:762px;top:1130px">
  <svg width="64" height="64" viewBox="0 0 64 64" fill="none" stroke="var(--navy)" stroke-width="2.5"><circle cx="32" cy="32" r="18"/><circle cx="32" cy="32" r="26" stroke-dasharray="7 5"/><circle cx="32" cy="26" r="5"/><path d="M32 31v14"/></svg>
  <span class="stem"></span>BI-as-a-service</div>
<div class="bump"></div>
<a class="btn" style="left:535px;top:1380px;width:130px">More info</a>

<section class="products">
  <div class="abs" style="top:58px;width:1200px;text-align:center"><span class="h2">Products overview</span></div>
</section>
<svg class="abs" style="left:0;top:1580px" width="1200" height="70" fill="none" stroke="var(--cyan-line)" stroke-width="1.5">
  <path d="M232 68V18a8 8 0 0 1 8-8h720a8 8 0 0 1 8 8v50"/><path d="M478 10v58"/><path d="M722 10v58"/>
</svg>
<div class="card" style="left:122px" role="img" aria-label="Photo of a woman reading data on a screen"><div class="abs" style="inset:0;background:linear-gradient(160deg,#1e3f6a,#6a5a55 55%,#203850)"></div><span>PUBLIC DATA ACCESS</span></div>
<div class="card" style="left:366px" role="img" aria-label="Photo of an analyst looking at climate charts on monitors"><div class="abs" style="inset:0;background:linear-gradient(160deg,#1d2a3a,#3e5e7a 50%,#b9b1a6)"></div><span>CLIMATE RISK SCAN</span></div>
<div class="card" style="left:609px" role="img" aria-label="Photo of coins balanced on a seesaw"><div class="abs" style="inset:0;background:linear-gradient(180deg,#e6ebe7,#cfd6d1 60%,#9fb0a6)"></div><span>PRICING BENCHMARK</span></div>
<div class="card" style="left:853px" role="img" aria-label="Photo of hands stacking coins on a table"><div class="abs" style="inset:0;background:linear-gradient(160deg,#2a3a55,#d8dde3 45%,#aeb9c4)"></div><span>COST MODEL</span></div>
<div class="pin" style="left:212px"><svg width="18" height="18" viewBox="0 0 24 24" fill="none" stroke="#fff" stroke-width="1.8"><circle cx="12" cy="8" r="4"/><path d="M4 21c1-5 4-7 8-7s7 2 8 7"/></svg></div>
<div class="pin" style="left:458px"><svg width="18" height="18" viewBox="0 0 24 24" fill="none" stroke="#fff" stroke-width="1.8"><circle cx="11" cy="11" r="7"/><path d="M16 16l5 5"/></svg></div>
<div class="pin" style="left:702px"><svg width="18" height="18" viewBox="0 0 24 24" fill="none" stroke="#fff" stroke-width="1.8"><path d="M4 20h16M6 16v-4M10 16V8M14 16v-6M18 16V5"/></svg></div>
<div class="pin" style="left:946px"><svg width="18" height="18" viewBox="0 0 24 24" fill="none" stroke="#fff" stroke-width="1.8"><rect x="4" y="5" width="16" height="15"/><path d="M4 10h16M9 14h2M13 14h2"/></svg></div>
<a class="btn" style="left:520px;top:1952px;width:159px">View products</a>

<div class="abs title-line" style="left:0;top:2092px;width:1200px"><span class="rule l"></span><span class="h2">Who is KORVEL for?</span><span class="rule r"></span></div>
<div class="who" style="left:135px;top:2155px">
  <svg width="58" height="58" viewBox="0 0 64 64" fill="none" stroke="var(--navy)" stroke-width="2.5"><circle cx="18" cy="10" r="4"/><circle cx="32" cy="10" r="4"/><circle cx="46" cy="10" r="4"/><path d="M8 24h48l-14 20H22z"/><path d="M32 28v14M28 32h6a3 3 0 0 1 0 6h-4"/></svg>
  <span class="stem"></span>Sales managers</div>
<div class="who" style="left:378px;top:2155px">
  <svg width="58" height="58" viewBox="0 0 64 64" fill="none" stroke="var(--navy)" stroke-width="2.5"><path d="M6 28 32 6l26 22"/><path d="M12 24v32h40V24"/><circle cx="32" cy="38" r="8"/><circle cx="32" cy="38" r="3"/></svg>
  <span class="stem"></span>Real estate<br>managers</div>
<div class="who" style="left:621px;top:2155px">
  <svg width="58" height="58" viewBox="0 0 64 64" fill="none" stroke="var(--navy)" stroke-width="2.5"><path d="M22 6h16l-4 10h-8z"/><path d="M26 16C12 24 10 54 30 54"/><path d="M34 16c8 4 12 12 12 18"/><path d="M30 28v18M26 32h6a3 3 0 0 1 0 6h-4"/><circle cx="46" cy="44" r="10"/><path d="M41 44l4 4 6-7"/></svg>
  <span class="stem"></span>Financials</div>
<div class="who" style="left:865px;top:2155px">
  <svg width="58" height="58" viewBox="0 0 64 64" fill="none" stroke="var(--navy)" stroke-width="2.5"><circle cx="32" cy="26" r="18"/><circle cx="32" cy="26" r="12"/><circle cx="32" cy="22" r="4"/><path d="M24 34c2-5 14-5 16 0"/><path d="M20 40l-6 16 8-3 4 7 4-10M44 40l6 16-8-3-4 7-4-10"/></svg>
  <span class="stem"></span>BI specialists</div>

<section class="community" role="img" aria-label="Photo of several hands stacked together in a circle of support"></section>
<div class="community-copy">
  <div class="h2">KORVEL &amp; the community</div>
  <p>KORVEL is a secure, integrated data platform designed to bring people, services, and information together—helping communities thrive.</p>
  <p>By bridging the gap between healthcare providers, housing associations, and local support services, KORVEL enables a more joined-up approach to care and wellbeing.</p>
</div>
<a class="btn" style="left:689px;top:2702px;width:194px">Join the community</a>

<div class="abs title-line" style="left:0;top:2880px;width:1200px"><span class="rule l"></span><span class="h2">What our clients says</span><span class="rule r"></span></div>
<div class="arrow" style="left:134px;top:3032px"><svg width="10" height="10" viewBox="0 0 10 10" fill="none" stroke="var(--teal)" stroke-width="1.5"><path d="M6.5 1.5 3 5l3.5 3.5"/></svg></div>
<div class="arrow" style="left:1034px;top:3032px"><svg width="10" height="10" viewBox="0 0 10 10" fill="none" stroke="var(--teal)" stroke-width="1.5"><path d="M3.5 1.5 7 5 3.5 8.5"/></svg></div>
<article class="quote" style="left:184px">
  <span class="qm">&#8220;</span>
  <div class="head"><div class="avatar" role="img" aria-label="Client portrait"></div><div><div class="name">MARA VINK</div><div class="stars">★★★★★</div></div></div>
  <p>Lorem ipsum dolor sit amet, consectetur adipiscing elit. Mauris blandit orci elit, eu fringilla ipsum viverra ultrices. Donec aliquet blandit tellus id lacinia. Duis ac sem sed ligula pulvinar rutrum id sed mi. Nunc elit lectus, bibendum non tincidunt sit amet, commodo sit amet felis.</p>
</article>
<article class="quote" style="left:609px">
  <span class="qm">&#8220;</span>
  <div class="head"><div class="avatar" role="img" aria-label="Client portrait"></div><div><div class="name">MARA VINK</div><div class="stars">★★★★★</div></div></div>
  <p>Lorem ipsum dolor sit amet, consectetur adipiscing elit. Mauris blandit orci elit, eu fringilla ipsum viverra ultrices. Donec aliquet blandit tellus id lacinia. Duis ac sem sed ligula pulvinar rutrum id sed mi. Nunc elit lectus, bibendum non tincidunt sit amet, commodo sit amet felis.</p>
</article>

<section class="cta">
  <div class="abs title-line" style="left:0;top:90px;width:1200px"><span class="rule l"></span><span class="h2">Ready to see KORVEL in action?</span><span class="rule r"></span></div>
  <p class="abs" style="top:135px;width:1200px;text-align:center;color:#fff;font-size:12px">Join the organisations using KORVEL to improve lives and transform services..</p>
  <a class="btn" style="left:459px;top:165px;width:137px">Plan a demo</a>
  <a class="btn white" style="left:604px;top:165px;width:138px">Start KORVEL</a>
</section>

<footer class="footer">
  <div class="brand" style="left:122px;top:40px;font-size:22px;color:#fff">KORVEL</div>
  <div class="abs" style="left:122px;top:100px;width:24px;height:24px;border-radius:50%;border:1.5px solid #fff"></div>
  <small class="abs" style="left:122px;top:135px;width:250px">Copyright 2025 KORVEL Data All Rights Reserved.<br>(Disclaimer, Privacy, Terms)</small>
  <span class="divider" style="left:375px"></span>
  <div class="col" style="left:403px;top:55px;width:230px"><h4>About us</h4><small style="margin-top:14px">KORVEL is a data analytics platform for the healthcare sector and social housing sector. It helps organizations unlock, analyze, and use data to make smarter decisions. KORVEL combines a scalable platform with intelligent tools, a professional community, and BI-as-a-Service.</small></div>
  <span class="divider" style="left:658px"></span>
  <div class="col" style="left:689px;top:55px"><h4>Contact us</h4>
    <div class="contact-row"><span class="ci"><svg width="12" height="12" viewBox="0 0 24 24" fill="none" stroke="#fff" stroke-width="2"><path d="M12 22s7-7 7-12a7 7 0 0 0-14 0c0 5 7 12 7 12z"/><circle cx="12" cy="10" r="2.5"/></svg></span>42 Linden Avenue, Westbrook</div>
    <div class="contact-row"><span class="ci"><svg width="12" height="12" viewBox="0 0 24 24" fill="none" stroke="#fff" stroke-width="2"><path d="M5 3h4l2 5-3 2a12 12 0 0 0 6 6l2-3 5 2v4a2 2 0 0 1-2 2A18 18 0 0 1 3 5a2 2 0 0 1 2-2z"/></svg></span>+10 55 410 2288</div>
    <div class="contact-row"><span class="ci"><svg width="12" height="12" viewBox="0 0 24 24" fill="none" stroke="#fff" stroke-width="2"><rect x="3" y="5" width="18" height="14"/><path d="M3 6l9 7 9-7"/></svg></span>hello@korvel-data.example</div>
  </div>
  <span class="divider" style="left:910px"></span>
  <div class="col" style="left:944px;top:55px"><h4>Main link</h4><small style="margin-top:12px;line-height:19px">What is KORVEL?<br>Products<br>Who it's for<br>Community<br>About us<br>Contact</small></div>
</footer>

</body>
</html>
```